Veltrano - Mechanic/Collision Center Business Card

We're looking for a business card design for our mechanic/ collision repair shop.

Can be with colours or monochromatic.

See the attached files.

Many thanks

```html
<!DOCTYPE html>
<html lang="en">
<head>
<meta charset="utf-8">
<title>Veltrano – Business Card</title>
<link href="https://fonts.googleapis.com/css2?family=Work+Sans:wght@400;500;700&display=swap" rel="stylesheet">
<style>
  :root {
    --backdrop: #3b332f;
    --card-black: #151515;
    --card-white: #ffffff;
    --brand-blue: #2d9fe0;
    --ink: #2b2b2b;
    --ink-soft: #4a4a4a;
    --white: #ffffff;
  }
  * { margin: 0; padding: 0; box-sizing: border-box; }
  html, body {
    width: 1200px; height: 716px; overflow: hidden;
    background: var(--backdrop);
    font-family: "Work Sans", sans-serif;
  }
  .canvas {
    width: 1200px; height: 716px;
    display: flex; align-items: center; justify-content: center; gap: 48px;
  }
  .card {
    width: 530px; height: 302px; position: relative;
    box-shadow: 0 14px 30px rgba(0,0,0,.45);
    overflow: hidden;
  }
  .card--front { background: var(--card-black); display: flex; align-items: center; justify-content: center; }
  .card--back { background: var(--card-white); }

  .brand { display: flex; align-items: center; gap: 12px; }
  .brand__mark { width: 18px; height: 18px; border-radius: 50%; background: var(--brand-blue); flex: none; }
  .brand__name {
    font-weight: 700; font-size: 40px; letter-spacing: 1px; text-transform: uppercase; line-height: 1;
  }
  .card--front .brand__name { color: var(--white); }
  .card--back .brand__name { color: var(--ink); font-size: 30px; }
  .card--back .brand { position: absolute; right: 30px; top: 112px; }

  .contact { position: absolute; left: 34px; top: 40px; }
  .contact__accent { position: absolute; left: 0; top: 44px; width: 8px; height: 30px; background: var(--brand-blue); }
  .contact__name { font-size: 24px; font-weight: 500; color: var(--brand-blue); text-transform: uppercase; line-height: 1.2; }
  .contact__title { font-size: 15px; color: var(--ink-soft); margin-top: 2px; }
  .contact__address { font-size: 15px; color: var(--ink); margin-top: 14px; line-height: 1.35; }
  .contact__list { list-style: none; margin-top: 8px; font-size: 15px; color: var(--ink); line-height: 1.45; }
  .contact__list li { display: flex; align-items: center; gap: 8px; }
  .contact__list svg { width: 11px; height: 11px; stroke: var(--brand-blue); fill: none; stroke-width: 1.6; flex: none; }
  .contact__web-name { color: var(--brand-blue); }
  .rule { position: absolute; left: 108px; right: 24px; top: 92px; height: 1px; background: var(--brand-blue); }
  .rule--low { left: 34px; top: 268px; right: 58px; }
</style>
</head>
<body>
<main class="canvas">
  <section class="card card--front" aria-label="Card front">
    <div class="brand">
      <span class="brand__mark"></span>
      <span class="brand__name">Veltrano</span>
    </div>
  </section>

  <section class="card card--back" aria-label="Card back">
    <span class="contact__accent"></span>
    <span class="rule"></span>
    <div class="contact">
      <h1 class="contact__name">Daniel Reyes</h1>
      <p class="contact__title">Director</p>
      <p class="contact__address">418 Birch Hollow Lane<br>Millbrook, PA 19321</p>
      <ul class="contact__list">
        <li><svg viewBox="0 0 12 12"><path d="M3 1 L5 3.5 L4 5 Q5.5 7.5 7 8 L8.5 7 L11 9 L9.5 11 Q3 10 1 2.5 Z"/></svg><span>06.41.73.20.85</span></li>
        <li><svg viewBox="0 0 12 12"><rect x="1" y="2.5" width="10" height="7"/><path d="M1 2.5 L6 6.5 L11 2.5"/></svg><span>info@veltrano.com</span></li>
        <li><svg viewBox="0 0 12 12"><circle cx="6" cy="6" r="5"/><path d="M1 6 H11 M6 1 Q3 6 6 11 Q9 6 6 1"/></svg><span>www.<span class="contact__web-name">veltrano</span>.com</span></li>
      </ul>
    </div>
    <div class="brand">
      <span class="brand__mark"></span>
      <span class="brand__name">Veltrano</span>
    </div>
    <span class="rule rule--low"></span>
  </section>
</main>
</body>
</html>
```